ko rim magazine

just need coupons of real customers made for my magazine, I have the layout or temp lets of the magazine i just need the coupons to be made and plug-in. i have examples, of the ads or coupons, I'm sure they will need to redone. and in a section of the magazine their in a church directory. with this section , i need the pic of the pastor plug in with their church information and in do have some ex-samples of that as well. with the websites of the businesses. if you need to grab an image from their site . you'll be able to do so. all of the business are in the upload section , these are small base business so a lot of the ads and logos need redone any way . so i will look at it and let you know.

P.S with the new coupons and logos I'm trying to impress these customers to stay with the magazine

Target Market(s)

small businesses

Requirements
Must have
• good graphics
Should not have
• not pixelated graphics

```html
<!DOCTYPE html>
<html lang="en">
<head>
<meta charset="utf-8">
<title>Church Directory</title>
<link href="https://fonts.googleapis.com/css2?family=Archivo+Black&family=Arimo:wght@400;700&display=swap" rel="stylesheet">
<style>
  :root {
    --paper: #f8e9cf;
    --brown: #5b3a2b;
    --frame: #7a5a4a;
    --card: #ffffff;
    --ink: #3b3b3b;
    --photo-light: #f4f1ee;
    --photo-dark: #3f3431;
  }
  * { box-sizing: border-box; margin: 0; padding: 0; }
  html, body { width: 849px; height: 1200px; overflow: hidden; }
  body {
    background: var(--paper);
    font-family: "Arimo", Arial, sans-serif;
    color: var(--ink);
    position: relative;
  }
  .directory-header {
    position: absolute; left: 0; top: 34px; width: 849px; height: 86px;
  }
  .book-icon { position: absolute; top: 0; width: 82px; height: 86px; }
  .book-icon.left { left: 37px; }
  .book-icon.right { left: 730px; }
  .directory-title {
    position: absolute; left: 128px; top: 14px; width: 592px;
    text-align: center;
    font-family: "Archivo Black", "Arial Black", sans-serif;
    font-size: 49px; line-height: 58px; letter-spacing: 0;
    color: var(--brown); white-space: nowrap;
  }
  .rule {
    position: absolute; left: 26px; width: 801px; height: 5px; background: var(--brown);
  }
  .rule.top { top: 151px; }
  .rule.bottom { top: 1148px; }
  .listing-grid {
    position: absolute; left: 23px; top: 188px;
    display: grid;
    grid-template-columns: 394px 394px;
    grid-auto-rows: 157px;
    column-gap: 15px; row-gap: 32px;
  }
  .listing {
    background: var(--card);
    border: 1px solid var(--frame);
    position: relative;
    overflow: hidden;
  }
  .pastor-photo {
    position: absolute; left: 8px; top: 8px; width: 131px; height: 140px;
    border: 1px solid var(--frame);
    background: linear-gradient(180deg, var(--photo-light) 0%, #b08d7b 45%, var(--photo-dark) 100%);
  }
  .listing.right .pastor-photo { width: 125px; }
  .listing-info {
    position: absolute; left: 150px; right: 4px; top: 0; bottom: 0;
    display: flex; flex-direction: column; justify-content: center;
    font-size: 14.5px; line-height: 17px;
  }
  .listing.right .listing-info { left: 143px; }
  .church-name, .pastor-name { font-weight: 700; white-space: nowrap; }
  .church-name { font-size: 14.5px; }
  .pastor-name { font-size: 13.4px; margin-bottom: 2px; }
  .listing-info.spaced p + p { margin-top: 8px; }
  .listing-info.compact { font-size: 10.6px; line-height: 12.3px; }
  .listing-info.compact .church-name,
  .listing-info.compact .pastor-name { font-size: 10.4px; margin: 0; }
  .listing-info.medium { font-size: 11.4px; line-height: 13.5px; }
  .listing-info.medium .church-name { font-size: 11.6px; }
  .listing-info.medium .pastor-name { font-size: 11px; margin-bottom: 4px; }
</style>
</head>
<body>
  <header class="directory-header">
    <svg class="book-icon left" viewBox="0 0 82 86" fill="none" stroke="#5b3a2b" stroke-width="3">
      <rect x="22" y="2" width="46" height="82" rx="2"/>
      <line x1="30" y1="2" x2="30" y2="84"/>
      <path d="M68 10h7v12h-7M68 26h5v12h-5M68 42h4v12h-4"/>
      <g><rect x="2" y="8" width="16" height="6" rx="3"/><rect x="2" y="20" width="16" height="6" rx="3"/><rect x="2" y="32" width="16" height="6" rx="3"/><rect x="2" y="44" width="16" height="6" rx="3"/><rect x="2" y="56" width="16" height="6" rx="3"/><rect x="2" y="68" width="16" height="6" rx="3"/></g>
      <circle cx="45" cy="33" r="7"/>
      <path d="M34 50c1-8 21-8 22 0z"/>
      <line x1="35" y1="58" x2="56" y2="58"/><line x1="35" y1="64" x2="56" y2="64"/>
    </svg>
    <h1 class="directory-title">CHURCH DIRECTORY</h1>
    <svg class="book-icon right" viewBox="0 0 82 86" fill="none" stroke="#5b3a2b" stroke-width="3">
      <rect x="22" y="2" width="46" height="82" rx="2"/>
      <line x1="30" y1="2" x2="30" y2="84"/>
      <path d="M68 10h7v12h-7M68 26h5v12h-5M68 42h4v12h-4"/>
      <g><rect x="2" y="8" width="16" height="6" rx="3"/><rect x="2" y="20" width="16" height="6" rx="3"/><rect x="2" y="32" width="16" height="6" rx="3"/><rect x="2" y="44" width="16" height="6" rx="3"/><rect x="2" y="56" width="16" height="6" rx="3"/><rect x="2" y="68" width="16" height="6" rx="3"/></g>
      <circle cx="45" cy="33" r="7"/>
      <path d="M34 50c1-8 21-8 22 0z"/>
      <line x1="35" y1="58" x2="56" y2="58"/><line x1="35" y1="64" x2="56" y2="64"/>
    </svg>
  </header>
  <div class="rule top"></div>

  <main class="listing-grid">
    <article class="listing left">
      <div class="pastor-photo" role="img" aria-label="Portrait of the pastor in a dark suit"></div>
      <div class="listing-info">
        <p class="church-name">Grace Harbor Baptist Church</p>
        <p class="pastor-name">Pastor : Dr. Warren L. Gaines</p>
        <p>1420 Linden Street Pittsburg,<br>Pa15208</p>
        <p>(412) 555-0142</p>
        <p>Sunday Worship Service 10:30 AM</p>
      </div>
    </article>
    <article class="listing right">
      <div class="pastor-photo" role="img" aria-label="Photo of the pastor and his wife"></div>
      <div class="listing-info">
        <p class="church-name">Zion Temple Church (ztc-lhs)</p>
        <p class="pastor-name">Pastor : Reverend Marcus Allen Reed</p>
        <p>3310 Harbor Street, Pittsburg,<br>PA. 15208</p>
        <p>(412) 555-0178</p>
        <p>Sunday Worship Service 8:00 AM &amp;<br>10:30 AM</p>
      </div>
    </article>

    <article class="listing left">
      <div class="pastor-photo" role="img" aria-label="Portrait of the pastor seated in a dark suit"></div>
      <div class="listing-info compact">
        <p class="church-name">Hope Community Missionary Baptist Church</p>
        <p class="pastor-name">Pastor : Reverend Calvin D. Morrison</p>
        <p>5120 Maple Grove Avenue Pittsburgh, PA 15208</p>
        <p>(412) 555 0190 - Church</p>
        <p>(412) 555 0191 - Fax</p>
        <p>In-Person Sunday Worship Service 9:00 AM &amp;<br>Replay 5:00 PM EST</p>
        <p>Wednesday Midweek Only Bible Study<br>2:00 AM - 1:00 PM</p>
        <p>Midweek Corporate Prayer 6:00 PM - 7: 00 PM</p>
      </div>
    </article>
    <article class="listing right">
      <div class="pastor-photo" role="img" aria-label="Photo of the pastor preaching at a wooden pulpit"></div>
      <div class="listing-info spaced">
        <p class="church-name">New Hope Baptist Church</p>
        <p class="pastor-name">Pastor : Dr. Samuel T. Whitfield Sr.</p>
        <p>906 Oakview Ave, Pittsburgh, PA.</p>
        <p>(412) 555-0123</p>
        <p>Sunday Worship Service 11:00AM</p>
      </div>
    </article>

    <article class="listing left">
      <div class="pastor-photo" role="img" aria-label="Portrait of the pastor in glasses and a dark suit"></div>
      <div class="listing-info medium">
        <p class="church-name">Living Word Church</p>
        <p class="pastor-name">Pastor : Reverend Dr. Thomas E. Bennett Jr.</p>
        <p>248 Elmwood Ave. / Pittsburgh, PA 15208</p>
        <p>(412) 555-0164</p>
        <p style="margin-top:30px">Sunday Worship Service 10:00 AM</p>
      </div>
    </article>
    <article class="listing right">
      <div class="pastor-photo" role="img" aria-label="Portrait of the pastor in a light grey jacket"></div>
      <div class="listing-info spaced" style="left:151px">
        <p class="church-name">Mount Olive Baptist Church</p>
        <p><b>Pastor</b> : Dr. Andre K. Foster</p>
        <p>1875 Chestnut Ave, Pittsburg, PA</p>
        <p>(412) 555-0137</p>
        <p>Sunday Worship Service 11:00AM</p>
      </div>
    </article>

    <article class="listing left">
      <div class="pastor-photo" role="img" aria-label="Portrait of the pastor in a pinstripe suit"></div>
      <div class="listing-info medium">
        <p class="church-name">Willow Street Missionary Baptist Church</p>
        <p class="pastor-name">Pastor : Reverend Dr. Gregory P. Hayes</p>
        <p>4025 Willow St. Pittsburgh, PA</p>
        <p>(412) 555-0182</p>
        <p>Church Service Join Us Virtually : Sunday Academy 7.30AM, Sunday Worship 9:00AM, 2:00PM, 7:00AM, 10:00PM, Monday 8:00AM, and 12:00PM Noon, Wednesdays at Noon Saturdays at 10:00PM</p>
      </div>
    </article>
    <article class="listing right">
      <div class="pastor-photo" role="img" aria-label="Photo of the pastor speaking at a pulpit"></div>
      <div class="listing-info spaced">
        <p class="church-name">St. Mark Baptist Church</p>
        <p><b>Pastor</b> : Rev. Lorraine Pratt</p>
        <p>5502 Ave, Pittsburg, PA</p>
        <p>(412) 555-0132</p>
        <p>Sunday Worship Service 10:30AM<br>Sunday School 8:30AM</p>
      </div>
    </article>

    <article class="listing left">
      <div class="pastor-photo" role="img" aria-label="Portrait of the pastor in a dark suit"></div>
      <div class="listing-info">
        <p class="church-name">Grace Harbor Baptist Church</p>
        <p class="pastor-name">Pastor : Dr. Warren L. Gaines</p>
        <p>1420 Linden Street Pittsburg,<br>Pa15208</p>
        <p>(412) 555-0142</p>
        <p>Sunday Worship Service 10:30 AM</p>
      </div>
    </article>
    <article class="listing right">
      <div class="pastor-photo" role="img" aria-label="Photo of the pastor and his wife"></div>
      <div class="listing-info">
        <p class="church-name">Zion Temple Church (ztc-lhs)</p>
        <p class="pastor-name">Pastor : Reverend Marcus Allen Reed</p>
        <p>3310 Harbor Street, Pittsburg,<br>PA. 15208</p>
        <p>(412) 555-0178</p>
        <p>Sunday Worship Service 8:00 AM &amp;<br>10:30 AM</p>
      </div>
    </article>
  </main>

  <div class="rule bottom"></div>
</body>
</html>
```